Sales Brochure

We are looking for an 8.5 x 11 folding brochure in a landscape orientation that advertises our product and service offerings. This brochure should have content on both sides.

This brochure would be left at prospect client's business, so it needs to be fresh, professional, and focused.

We have attached two 1-page inserts that we would like you to use for inspiration for the written content in the brochure. We would like the main theme of the brochure to focus on professional, repeatable, and quality IT support for business.

The brochure should have the prospective clients email or call (will provide number and email to winner) to get additional information.

Please be creative with both the content and the design.

Went on vacation/holiday

```html
<!DOCTYPE html>
<html lang="en">
<head>
<meta charset="utf-8">
<title>Nortesa – IT Support Brochure</title>
<link rel="stylesheet" href="https://fonts.googleapis.com/css2?family=Montserrat:wght@400;500;600&display=swap">
<style>
  :root{
    --blue:#1b8fdb;
    --blue-deep:#0f6fc6;
    --blue-light:#2ea3ea;
    --icon-tint:#d6ebf9;
    --icon-fade:#f3f3f3;
    --ink:#222;
    --muted:#6b6b6b;
    --stage:#e8e9eb;
    --white:#fff;
  }
  *{margin:0;padding:0;box-sizing:border-box}
  html,body{width:860px;height:1200px;overflow:hidden}
  body{background:var(--stage);font-family:"Montserrat",sans-serif;color:var(--ink);position:relative}
  .brochure-panel{position:absolute;left:0;top:300px;width:860px;height:600px;background:var(--white)}
  .header-band{position:absolute;left:0;top:0;width:860px;height:106px;
    background:linear-gradient(100deg,var(--blue-deep) 0%,var(--blue-light) 50%,var(--blue-deep) 100%);
    clip-path:polygon(0 0,100% 0,100% 70px,50% 106px,0 70px)}
  .brand{position:absolute;left:88px;top:20px;color:var(--white)}
  .brand-name{display:flex;align-items:center;gap:8px;font-size:22px;font-weight:500;letter-spacing:1.5px}
  .brand-dot{width:14px;height:14px;border-radius:50%;background:var(--white)}
  .brand-tagline{margin-top:3px;margin-left:34px;font-size:11.5px;font-weight:500;letter-spacing:.2px}
  .contact{position:absolute;right:82px;top:26px;color:var(--white);text-align:center}
  .contact-phone{font-size:18px;font-weight:500;letter-spacing:.3px}
  .contact-web{margin-top:4px;font-size:11.5px;font-weight:500}
  .intro{position:absolute;left:37px;top:122px;width:796px;font-size:12.6px;line-height:19px;color:var(--muted)}
  .lead-in{position:absolute;left:37px;top:199px;font-size:12.6px;font-weight:500;color:#444}
  .services{position:absolute;left:0;top:250px;width:860px;display:flex;justify-content:space-around;padding:0 14px}
  .service{width:176px;text-align:center}
  .service-visual{width:118px;height:118px;margin:0 auto;border-radius:50%;
    background:radial-gradient(circle at 50% 45%,var(--icon-tint) 0%,var(--icon-fade) 72%)}
  .service-title{margin-top:48px;font-size:12.5px;font-weight:500;color:var(--blue);letter-spacing:.2px}
  .service-copy{margin-top:22px;font-size:9.8px;line-height:14.6px;color:var(--ink)}
  .service-copy p+p{margin-top:14.6px}
</style>
</head>
<body>
<main class="brochure-panel">
  <header class="header-band">
    <div class="brand">
      <div class="brand-name"><span class="brand-dot"></span>NORTESA</div>
      <div class="brand-tagline">LEAVE IT TO THE PROFESSIONALS.</div>
    </div>
    <div class="contact">
      <div class="contact-phone">403.555.0182</div>
      <div class="contact-web">SALES@NORTESA.COM • WWW.NORTESA.COM</div>
    </div>
  </header>

  <p class="intro">We provide responsive, quality IT solutions to Calgary, Airdrie, Three Hills and the surrounding areas. Our unique CoreCARE™ service plans provide fast response times, and our project services provide expert IT help at an affordable price. Professionalism and reliable customer service is our standard.</p>
  <p class="lead-in">Here are a few ways in which we take care of your IT needs:</p>

  <section class="services">
    <article class="service">
      <div class="service-visual" role="img" aria-label="Line illustration of a desktop monitor with a support agent"></div>
      <h2 class="service-title">DESKTOP SUPPORT</h2>
      <div class="service-copy">
        <p>Available 24/7</p>
        <p>Regular face-to-face IT check ups</p>
        <p>Satisfaction surveys ensure you are pleased with the quality of the desktop support you are receiving.</p>
      </div>
    </article>

    <article class="service">
      <div class="service-visual" role="img" aria-label="Line illustration of cloud, server and email systems"></div>
      <h2 class="service-title">SYSTEMS MANAGEMENT</h2>
      <div class="service-copy">
        <p>We make our expertise in system and network technologies (such as email, servers, cloud, wireless, printing and remote access) work for you.</p>
      </div>
    </article>

    <article class="service">
      <div class="service-visual" role="img" aria-label="Line illustration of secured data storage"></div>
      <h2 class="service-title">DATA PROTECTION</h2>
      <div class="service-copy">
        <p>We offer cost effective solutions to make sure your information is backed up securely.<br>We ensure that backups are run properly and consistently, and monitor those backups on a daily basis.</p>
      </div>
    </article>

    <article class="service">
      <div class="service-visual" role="img" aria-label="Line illustration of a project checklist"></div>
      <h2 class="service-title">IT PROJECTS</h2>
      <div class="service-copy">
        <p>We plan, manage and implement all your technology projects.<br>We promise to meet your stated objectives, on time and on budget.</p>
      </div>
    </article>
  </section>
</main>
</body>
</html>
```